Sandwich Board and Poster design promoting a medical aesthetic clinic

I am looking for a clean, modern and relaxing design promoting a medical physician-led aesthetic clinic.
Services offered are neuromodulator treatment (Quelvo) and Dermal Fillers.
Logo must be included.
Use the tag line "Refresh your look, revive your spirit."
Address is 204-205 27361 92 Ave, Surrey, V7K 2M4
604-555-0148
email - info@lumawellpine.ca
www.lumawellpine.ca

```html
<!DOCTYPE html>
<html lang="en">
<head>
<meta charset="utf-8">
<title>Lumawell Pine – Poster</title>
<link rel="stylesheet" href="https://fonts.googleapis.com/css2?family=Montserrat:wght@300;400;500;700;800&display=swap">
<style>
  :root {
    --backdrop: #c9c9cb;
    --paper: #ffffff;
    --navy: #243f60;
    --gold: #c9a227;
    --gold-deep: #b8901f;
    --mist: #e9e9ea;
    --ink: #1f2a3a;
  }
  html, body {
    margin: 0;
    padding: 0;
    width: 1200px;
    height: 2547px;
    overflow: hidden;
    background: var(--backdrop);
  }
  .poster {
    position: absolute;
    left: 100px;
    top: 565px;
    width: 1000px;
    height: 1416px;
    box-shadow: 0 14px 30px rgba(0,0,0,0.25);
    display: block;
  }
  .brand-name { font-family: "Montserrat", sans-serif; font-weight: 500; fill: var(--ink); letter-spacing: 9px; }
  .headline { font-family: "Montserrat", sans-serif; font-weight: 800; fill: var(--gold); }
  .service { font-family: "Montserrat", sans-serif; font-weight: 300; fill: #ffffff; }
  .contact { font-family: "Montserrat", sans-serif; font-weight: 700; fill: var(--navy); }
  .address { font-family: "Montserrat", sans-serif; font-weight: 400; fill: #ffffff; letter-spacing: 5px; }
</style>
</head>
<body>
<svg class="poster" viewBox="0 0 893 1265" xmlns="http://www.w3.org/2000/svg">
  <defs>
    <linearGradient id="faces-left" x1="0" y1="0" x2="1" y2="0">
      <stop offset="0" stop-color="#dcdcdd"/>
      <stop offset="1" stop-color="#ffffff"/>
    </linearGradient>
    <linearGradient id="faces-right" x1="1" y1="0" x2="0" y2="0">
      <stop offset="0" stop-color="#dcdcdd"/>
      <stop offset="1" stop-color="#ffffff"/>
    </linearGradient>
    <linearGradient id="treatment-tones" x1="0" y1="0" x2="1" y2="1">
      <stop offset="0" stop-color="#9fd3ea"/>
      <stop offset="0.45" stop-color="#c99272"/>
      <stop offset="1" stop-color="#6b4a35"/>
    </linearGradient>
    <clipPath id="arch-window">
      <path d="M138 680 V582 A310 310 0 0 1 758 582 V680 Z"/>
    </clipPath>
  </defs>

  <!-- upper white field -->
  <rect class="paper" x="0" y="0" width="893" height="690" fill="var(--paper)"/>
  <rect x="0" y="0" width="300" height="690" fill="url(#faces-left)" role="img" aria-label="Soft faded portraits of women in profile"/>
  <rect x="593" y="0" width="300" height="690" fill="url(#faces-right)" role="img" aria-label="Soft faded portraits of women in profile"/>

  <!-- brand -->
  <text class="brand-name" x="446" y="200" font-size="34" text-anchor="middle">LUMAWELL PINE</text>

  <!-- treatment photo in arch -->
  <g clip-path="url(#arch-window)">
    <rect x="130" y="260" width="640" height="430" fill="url(#treatment-tones)" role="img" aria-label="Patient receiving a forehead injection treatment"/>
  </g>
  <path d="M128 680 C120 620 118 560 140 490 A318 318 0 0 1 520 262" fill="none" stroke="var(--gold)" stroke-width="9" stroke-linecap="round"/>
  <path d="M565 268 A318 318 0 0 1 772 430 C785 500 782 610 762 680" fill="none" stroke="var(--gold)" stroke-width="9" stroke-linecap="round"/>
  <path d="M108 680 C100 620 100 560 110 530" fill="none" stroke="var(--gold)" stroke-width="3" stroke-linecap="round"/>

  <!-- navy panel -->
  <rect x="0" y="687" width="893" height="578" fill="var(--navy)"/>
  <rect x="0" y="683" width="893" height="8" fill="var(--gold)"/>
  <rect x="40" y="725" width="740" height="5" rx="2.5" fill="var(--gold)"/>
  <rect x="180" y="765" width="440" height="3.5" rx="1.75" fill="var(--gold)"/>
  <rect x="325" y="806" width="220" height="3" rx="1.5" fill="var(--gold)"/>

  <text class="headline" x="446" y="884" font-size="57" text-anchor="middle">REFRESH YOUR LOOK,</text>
  <text class="headline" x="446" y="960" font-size="57" text-anchor="middle">REVIVE YOUR SPIRIT</text>

  <!-- services -->
  <rect x="88" y="1010" width="62" height="64" rx="10" fill="var(--gold-deep)" opacity="0.35" role="img" aria-label="Neuromodulator treatment icon"/>
  <text class="service" x="173" y="1036" font-size="25">NEUROMODULATOR</text>
  <text class="service" x="173" y="1068" font-size="25">TREATMENT (QUELVO)</text>
  <rect x="480" y="1007" width="4" height="72" fill="#ffffff"/>
  <rect x="500" y="1010" width="72" height="64" rx="10" fill="var(--gold-deep)" opacity="0.35" role="img" aria-label="Dermal fillers icon"/>
  <text class="service" x="583" y="1053" font-size="25">DERMAL FILLERS</text>

  <!-- contact strip -->
  <rect x="0" y="1121" width="893" height="57" fill="var(--paper)"/>
  <g fill="var(--gold)">
    <path d="M68 1141 l5 -2 l3 6 l-3 2 q2 5 7 8 l2 -3 l6 3 l-2 5 q-12 0 -18 -19z"/>
    <rect x="286" y="1143" width="18" height="13" rx="1"/>
  </g>
  <path d="M286 1144 l9 7 l9 -7" fill="none" stroke="#ffffff" stroke-width="1.6"/>
  <g fill="none" stroke="var(--gold)" stroke-width="1.8">
    <circle cx="584" cy="1150" r="8"/>
    <ellipse cx="584" cy="1150" rx="3.5" ry="8"/>
    <line x1="576" y1="1150" x2="592" y2="1150"/>
  </g>
  <text class="contact" x="93" y="1157" font-size="19.5">604-555-0148</text>
  <text class="contact" x="311" y="1157" font-size="19.5">info@lumawellpine.ca</text>
  <text class="contact" x="597" y="1157" font-size="19.5">www.lumawellpine.ca</text>

  <text class="address" x="446" y="1225" font-size="20" text-anchor="middle">204-205 27361 92 Ave, Surrey, V7K 2M4</text>
</svg>
</body>
</html>
```